Castastrophe General Contractor needs leave behind for sales

Will respond quickly to designer inquires
Fast winning selection
Will notify all of winning selection

Catastrophe Restoration General Contractor offering specialized services to the insurance industry. Sales meeting leave behind flyer for presentation to insurance agents. We would like for agents to refer policyholders to our company for complete residential and commercial restoration projects.

Some copy uploaded for reference. 5.5" x 8.5" approx - double sided color w/ sales business card reproduced on back side. Approved / Preferred Contractor for Coastwide, Vantora, RQBT & Selvo insurance companies.

Bramblecourt Company is a general contractor specialized in the restoration industry for both residential and commercial properties.
We have incorporated the best technology tools and partnered with a network of industry professionals across the country to provide the most efficient and comprehensive service available.
Website under construction: www.thebramblecourtcompany.example

Target Market(s)

Insurance Sale Agents

Industry/Entity Type

Residential

Requirements
Must have
• Coastwide, Vantora & RQBT & Hadley Vortan logos. Space to reproduce business card on back.. Looking for concept deign where we can work w/ local designer if necessary to finalize. Open to different sized flyer dependent on design.

```html
<!DOCTYPE html>
<html lang="en">
<head>
<meta charset="utf-8">
<title>Bramblecourt Company – Agent Support Flyer</title>
<link rel="stylesheet" href="https://fonts.googleapis.com/css2?family=Open+Sans:wght@400;600;700&family=Roboto+Condensed:wght@700&display=swap">
<style>
  :root{
    --bg:#e9e6e1;
    --blue:#3f7ea6;
    --blue-dark:#2f6a8f;
    --navy:#23406b;
    --green:#6c9b3c;
    --yellow:#f6b81c;
    --ink:#1e1e1e;
    --white:#ffffff;
    --grey:#d9dbdd;
  }
  *{box-sizing:border-box;margin:0;padding:0}
  html,body{width:957px;height:1200px;overflow:hidden}
  body{background:var(--bg);font-family:"Open Sans",Arial,sans-serif;color:var(--ink);position:relative}
  .card{position:absolute;left:102px;width:753px;background:var(--white);overflow:hidden;box-shadow:0 2px 8px rgba(0,0,0,.18)}
  .front{top:95px;height:483px}
  .back{top:615px;height:487px}
  .abs{position:absolute}

  /* front */
  .headline{left:24px;top:14px;font-family:"Roboto Condensed","Arial Narrow",sans-serif;font-weight:700;color:var(--blue);font-size:22px;line-height:25px;text-transform:uppercase}
  .headline .sub{margin-top:12px}
  .brand{right:22px;top:30px;display:flex;align-items:center;gap:10px;white-space:nowrap}
  .brand-mark{width:30px;height:30px;background:var(--yellow)}
  .brand-name{font-family:"Open Sans",Arial,sans-serif;font-weight:600;font-size:18px;color:var(--blue);white-space:nowrap}
  .photo-front{left:0;top:118px;width:463px;height:320px;background:linear-gradient(180deg,#c9ccd0 0%,#b4b6b8 38%,#8d8f8c 60%,#6f7f4e 78%,#7a6f5c 100%)}
  .panel-front{left:463px;top:118px;width:290px;height:330px;background:var(--green)}
  .box{background:var(--yellow);border-radius:10px;left:475px;width:266px;padding:10px 12px}
  .box h3{font-family:"Roboto Condensed","Arial Narrow",sans-serif;font-size:16px;color:var(--ink);text-transform:uppercase;margin-bottom:6px}
  .box .tag{font-size:11.5px;font-weight:700;margin:-2px 0 6px}
  .box1{top:128px;height:146px}
  .box2{top:280px;height:146px}
  .checks{list-style:none}
  .checks li{position:relative;padding-left:18px;font-size:10.5px;line-height:13px;margin-bottom:6px}
  .checks li::before{content:"";position:absolute;left:0;top:1px;width:11px;height:11px;background:var(--white);border:1px solid #555}
  .checks li::after{content:"";position:absolute;left:3px;top:2px;width:4px;height:7px;border:solid var(--ink);border-width:0 2px 2px 0;transform:rotate(40deg)}
  .box1 .checks{padding-right:14px}
  .contact-bar{left:0;top:430px;width:310px;height:40px;background:var(--yellow);clip-path:polygon(0 0,100% 0,94% 100%,0 100%);font-weight:700;font-size:16px;padding:9px 0 0 36px;white-space:nowrap}
  .contact-bar b{font-size:20px}
  .email-bar{left:296px;top:442px;width:457px;height:41px;background:var(--blue-dark);clip-path:polygon(4% 0,100% 0,100% 100%,0 100%);color:var(--white);font-weight:700;font-size:17px;text-align:right;padding:9px 18px 0 0;white-space:nowrap}

  /* back */
  .stripe{left:0;top:0;width:753px;height:8px;background:var(--blue)}
  .panel-back{left:0;top:8px;width:375px;height:402px;background:var(--green);padding:20px 18px}
  .pill{display:inline-block;background:var(--blue);color:var(--white);font-weight:700;font-size:14px;padding:3px 14px;border-radius:0 12px 12px 0;margin:0 0 8px -18px;width:230px}
  .panel-back .checks li{color:var(--white);font-size:10.5px;padding-left:20px;margin-bottom:8px}
  .panel-back .checks li::before{border-color:#3a5a22}
  .panel-back .checks{width:240px;margin-bottom:14px}
  .photo-back{left:375px;top:0;width:378px;height:410px;background:linear-gradient(180deg,#9fb8cf 0%,#e9c7a8 30%,#8a8f86 55%,#4a5340 80%,#3b4a2c 100%)}
  .biz{left:30px;top:315px;width:330px;height:88px;border-radius:14px;background:linear-gradient(180deg,#f4f5f6,var(--grey));padding:12px 14px 0 60px}
  .biz .phone{font-size:14px;font-weight:600;white-space:nowrap}
  .biz .phone b{font-size:15px}
  .biz .small{font-size:8px;line-height:11px;margin-top:4px;white-space:nowrap}
  .biz-brand{position:absolute;right:14px;bottom:8px;display:flex;align-items:center;gap:6px}
  .biz-brand .brand-mark{width:14px;height:14px}
  .biz-brand .brand-name{font-size:13px}
  .logos{left:0;top:410px;width:753px;height:77px;display:flex;align-items:center;justify-content:space-around;padding:0 14px}
  .partner{font-family:"Open Sans",Arial,sans-serif;font-weight:700;font-size:15px;color:var(--navy);white-space:nowrap}
  .badge-sq{width:30px;height:42px;background:var(--navy);border-radius:3px}
  .badge-circ{width:40px;height:40px;border-radius:50%;background:var(--blue)}
</style>
</head>
<body>
  <section class="card front">
    <div class="abs headline">
      <div>Preferred Contractor Agent Support</div>
      <div class="sub">Providing claims support during<br>and after a CAT event</div>
    </div>
    <div class="abs brand"><span class="brand-mark"></span><span class="brand-name">Bramblecourt Company</span></div>
    <div class="abs photo-front" role="img" aria-label="Photo of a large two-storey residence with a paved driveway and lawn"></div>
    <div class="abs panel-front"></div>
    <div class="abs box box1">
      <h3>Agent Support Services</h3>
      <ul class="checks">
        <li>Guaranteed next day inspections from time of notification</li>
        <li>Damage status reporting directly back to Agent</li>
        <li>Assist policy holder in filing claim to CAT desk</li>
      </ul>
    </div>
    <div class="abs box box2">
      <h3>Agent Benefits:</h3>
      <p class="tag">Greater Satisfaction, Increased Retention</p>
      <ul class="checks">
        <li>Increase policyholder satisfaction</li>
        <li>Demonstrate a greater commitment to customer satisfaction</li>
        <li>Follow up on outcome beyond the closing of a claim</li>
      </ul>
    </div>
    <div class="abs contact-bar">Contact us: <b>(800) 555-0148</b></div>
    <div class="abs email-bar">info@bramblecourtcompany.example</div>
  </section>

  <section class="card back">
    <div class="abs stripe"></div>
    <div class="abs panel-back">
      <div class="pill">Enhanced Efficiency</div>
      <ul class="checks">
        <li>Increase efficiency in moving from claim to restoration completion</li>
        <li>“In-house” systems closely linked to the insurer or administrator</li>
        <li>Shorten the timeline from claims settlement to finished repairs</li>
      </ul>
      <div class="pill">Increased Quality Control</div>
      <ul class="checks">
        <li>Pre-screened and credentialed for license, insurance, and financial stability</li>
        <li>Monitored performance and control standards for higher-quality outcomes</li>
        <li>Background verification on all staff and field representatives</li>
      </ul>
    </div>
    <div class="abs photo-back" role="img" aria-label="Photo of a stone and shingle craftsman-style home at sunset with landscaped garden"></div>
    <div class="abs biz">
      <div class="phone">Call us: <b>(800) 555-0148</b></div>
      <div class="small">info@bramblecourtcompany.example<br>www.thebramblecourtcompany.example</div>
      <div class="biz-brand"><span class="brand-mark"></span><span class="brand-name">Bramblecourt Company</span></div>
    </div>
    <div class="abs logos">
      <span class="badge-sq"></span>
      <span class="partner">Selvo</span>
      <span class="partner">Hadley Vortan</span>
      <span class="partner">Coastwide</span>
      <span class="partner">RQBT</span>
      <span class="badge-circ"></span>
      <span class="partner">Vantora</span>
      <span class="badge-circ"></span>
      <span class="badge-circ"></span>
    </div>
  </section>
</body>
</html>
```